Retainer Care Instructions

Please make this PDF - more modern and easy to read for patients. Our demographic is predominately adolescents. All the information is important and text needs to remain relatively the same - can be simplified. Here is a link to care instructions that look nice https://www.brightpath-grins.com/resources

Target Market(s)

Parents and Children

Industry/Entity Type

Orthodontics

Colors
0054AA
0677BA
7BADD7
CADEEF
E8F1F8

Requirements
Must have
• Simple and clear
Nice to have
• Add graphics and images to look more modern
Should not have
• Graphics to demonstrate

```html
<!DOCTYPE html>
<html lang="en">
<head>
<meta charset="utf-8">
<title>Looking After Your Retainers</title>
<link href="https://fonts.googleapis.com/css2?family=Poppins:wght@400;500;600;700&display=swap" rel="stylesheet">
<style>
  :root {
    --navy: #0054AA;
    --blue: #0677BA;
    --sky: #7BADD7;
    --mist: #CADEEF;
    --ice: #E8F1F8;
    --ink: #3f4348;
    --grey: #a3a5a8;
    --rule: #b9bcc0;
    --alert: #e0201b;
    --caution: #fdd650;
    --white: #ffffff;
  }
  * { box-sizing: border-box; margin: 0; padding: 0; }
  html, body { width: 1038px; height: 1200px; overflow: hidden; background: var(--white); }
  body { font-family: "Poppins", sans-serif; color: var(--ink); }

  .sheet { position: relative; width: 1038px; height: 1200px; padding: 0 78px; }
  .sheet__tab { position: absolute; top: 0; right: 78px; width: 80px; height: 9px; background: var(--blue); }
  .sheet__base { position: absolute; left: 0; bottom: 0; width: 100%; height: 8px; background: var(--navy); }

  .masthead { display: flex; justify-content: space-between; align-items: flex-start; padding-top: 40px; height: 140px; }
  .brand { display: flex; align-items: center; gap: 14px; margin-top: 14px; }
  .brand__mark { width: 28px; height: 28px; background: var(--blue); }
  .brand__name { font-size: 38px; font-weight: 600; color: var(--grey); letter-spacing: -0.5px; line-height: 1; }
  .masthead__web { display: flex; align-items: center; gap: 8px; font-size: 17px; color: var(--ink); margin-top: 4px; }
  .masthead__web svg { width: 14px; height: 14px; }

  .title-band { background: var(--blue); height: 64px; display: flex; align-items: center; justify-content: center; }
  .title-band h1 { color: var(--white); font-size: 37px; font-weight: 700; letter-spacing: 0.2px; }

  .intro { display: flex; gap: 28px; margin-top: 32px; }
  .intro__badge { flex: 0 0 236px; height: 186px; border: 1.5px solid #d9dcdf; border-radius: 8px; display: flex; align-items: center; justify-content: center; }
  .intro__badge span { font-size: 17px; font-weight: 600; color: var(--ink); text-align: center; line-height: 1.3; }
  .intro__text { flex: 1; }

  p { font-size: 16px; line-height: 1.45; text-align: justify; }
  .lead { font-weight: 600; }
  h2 { font-size: 17px; font-weight: 700; color: var(--navy); text-transform: uppercase; line-height: 1.4; }
  h2.h2--blue { color: var(--blue); }
  .block { margin-top: 16px; }
  .block h2 { margin-bottom: 2px; }
  .left p { text-align: left; }
  .left p + p { margin-top: 10px; }

  .warning { display: flex; gap: 34px; padding: 16px 0 18px 8px; margin-top: 20px; border-top: 1.5px solid var(--rule); border-bottom: 1.5px solid var(--rule); }
  .warning svg { flex: 0 0 112px; height: 96px; margin-top: 8px; }
  .warning h3 { color: var(--alert); font-size: 18px; font-weight: 700; margin-bottom: 4px; }
  .warning p { text-align: left; }

  .contact { display: flex; justify-content: space-between; padding-top: 16px; font-size: 17px; line-height: 1.45; }
  .contact__item { display: flex; gap: 10px; align-items: flex-start; }
  .contact__item svg { width: 15px; height: 15px; margin-top: 5px; flex: 0 0 15px; }
  .contact__col { width: 370px; }
</style>
</head>
<body>
<div class="sheet">
  <div class="sheet__tab"></div>

  <header class="masthead">
    <div class="brand">
      <div class="brand__mark"></div>
      <div class="brand__name">Northlane Orthodontics</div>
    </div>
    <div class="masthead__web">
      <svg viewBox="0 0 16 16" fill="none" stroke="#0677BA" stroke-width="1.4"><circle cx="8" cy="8" r="6.5"/><ellipse cx="8" cy="8" rx="3" ry="6.5"/><line x1="1.5" y1="8" x2="14.5" y2="8"/></svg>
      www.northlane-ortho.com.au
    </div>
  </header>

  <div class="title-band"><h1>LOOKING AFTER YOUR RETAINERS</h1></div>

  <section class="intro">
    <div class="intro__badge"><span>Northlane<br>Orthodontics</span></div>
    <div class="intro__text">
      <p class="lead">The braces are off... it’s retainer time!!!!</p>
      <p>Always wear your retainer as instructed by your orthodontist. Remember to take your retainer out when eating and playing sport</p>
      <div class="block">
        <h2>DO NOT LOSE YOUR RETAINER!!!</h2>
        <p>The cost of your first retainers is covered in the fee for your treatment. However, if they are lost or broken and need replacement, this will incur an additional fee of $300 for a new one and we will have to take a new impression, So please look after it!!!!</p>
      </div>
    </div>
  </section>

  <section class="block left">
    <h2>ALWAYS STORE IN THE RETAINER CONTAINER PROVIDED</h2>
    <p>Clean your Retainer regularly, using a tooth brush and soaking it in a retainer cleaner such as- FreshDent, or any denture cleaning tablet . If it is not fitting, call us to arrange to have it checked and adjusted. Always go to your retainer check appointments, and we will tighten the retainer. So don’t forget your RETAINER!!!</p>
  </section>

  <section class="block left">
    <h2 class="h2--blue">IF YOU WANT TO KEEP YOUR TEETH STRAIGHT NEVER THROW YOUR RETAINERS AWAY!<br>IT’S UP TO YOU FROM HERE ON...<br>WHY IS THIS NEEDED?</h2>
    <p>Long-term clinical research shows that no matter how well teeth are straightened, they will show a tendency for some movement over many years (probably throughout life). By the way, this also occurs with teeth that haven’t had any orthodontic treatment. This tooth movement often shows up as an increase in crowding of the front teeth, by trying your retainers in every so often- and if neces- sary wearing them occasionally- you can keep your teeth straight for the years ahead.</p>
    <p>Cleaning tablets - Drop one tablet into enough warm (Not Hot) water to cover the appliance place appliance into the bubbling solution Leave for 10-15 mins and appliance is clean and odor free rinse thoroughly with running water</p>
  </section>

  <section class="warning">
    <svg viewBox="0 0 128 110" aria-hidden="true">
      <path d="M64 8 L122 102 L6 102 Z" fill="var(--caution)" stroke="#111" stroke-width="8" stroke-linejoin="round"/>
      <rect x="59" y="38" width="10" height="36" rx="5" fill="#111"/>
      <circle cx="64" cy="86" r="6" fill="#111"/>
    </svg>
    <div>
      <h3>Warnings:</h3>
      <p>DO NOT PLACE TABLETS IN MOUTH. Do not use to clean natural teeth,<br>Keep product out of reach of children. In case of accidental ingestion seek professional assistance or contact poison centre immediately 13-00-482</p>
    </div>
  </section>

  <footer class="contact">
    <div class="contact__item">
      <svg viewBox="0 0 16 16" fill="none" stroke="#0677BA" stroke-width="1.4"><path d="M8 15 C4 10 3 8 3 6 a5 5 0 0 1 10 0 c0 2 -1 4 -5 9z"/><circle cx="8" cy="6" r="1.8"/></svg>
      <div>48 Kestrel Road<br>MAPLEVALE VIC 3999</div>
    </div>
    <div class="contact__col">
      <div class="contact__item">
        <svg viewBox="0 0 16 16" fill="none" stroke="#0677BA" stroke-width="1.4"><path d="M3 2 h3 l1.5 3.5 -2 1.5 a8 8 0 0 0 3.5 3.5 l1.5 -2 3.5 1.5 v3 a1 1 0 0 1 -1 1 A12 12 0 0 1 2 3 a1 1 0 0 1 1 -1z"/></svg>
        <div>9000 4821</div>
      </div>
      <div class="contact__item">
        <svg viewBox="0 0 16 16" fill="none" stroke="#0677BA" stroke-width="1.4"><rect x="1.5" y="3.5" width="13" height="9"/><path d="M1.5 3.5 L8 9 L14.5 3.5"/></svg>
        <div>hello@northlane-ortho.com.au</div>
      </div>
    </div>
  </footer>

  <div class="sheet__base"></div>
</div>
</body>
</html>
```